Letter Head Design

I need a letter head design based on my company logo that I attached.
Include phone number: (403)582-3140
Address: 417 Brindlewood Avenue NE, Calgary, Alberta, Canada, T3M 4K8

Industry/Entity Type

It Company

```html
<!DOCTYPE html>
<html lang="en">
<head>
<meta charset="utf-8">
<title>Brightfold Interiors Corp. Letterhead</title>
<link rel="stylesheet" href="https://fonts.googleapis.com/css2?family=Source+Sans+3:wght@400;600;700&display=swap">
<style>
  :root {
    --backdrop: #ffffff;
    --paper: #ffffff;
    --brand-green: #5cb21e;
    --brand-green-light: #7cc832;
    --brand-blue: #1a5fae;
    --brand-blue-deep: #0b4fa3;
    --ink: #000000;
    --ink-body: #555555;
    --ink-heading: #7a7a7a;
    --ink-contact: #333333;
  }
  * { margin: 0; padding: 0; box-sizing: border-box; }
  html, body {
    width: 1200px;
    height: 1071px;
    overflow: hidden;
    background: var(--backdrop);
    font-family: "Source Sans 3", "Myriad Pro", Arial, sans-serif;
  }
  .letterhead {
    position: absolute;
    left: 328px;
    top: 153px;
    width: 544px;
    height: 768px;
    background: var(--paper);
    overflow: hidden;
  }
  .brand {
    position: absolute;
    left: 39px;
    top: 39px;
    height: 52px;
    display: flex;
    align-items: center;
    gap: 12px;
  }
  .brand-square {
    width: 30px;
    height: 30px;
    background: var(--brand-green);
    flex: none;
  }
  .brand-name {
    font-size: 16px;
    font-weight: 600;
    color: var(--brand-blue);
    line-height: 17px;
  }
  .contact {
    position: absolute;
    left: 259px;
    top: 58px;
    font-size: 8.4px;
    line-height: 11px;
    font-weight: 400;
    font-style: normal;
    color: var(--ink-contact);
  }
  .letter-title {
    position: absolute;
    left: 115px;
    top: 125px;
    font-size: 12.5px;
    font-weight: 700;
    color: var(--ink-heading);
  }
  .sidebar {
    position: absolute;
    left: 20px;
    top: 154px;
    width: 74px;
    text-align: right;
    font-size: 8px;
    line-height: 11.5px;
    color: var(--ink);
  }
  .sidebar-item { margin-bottom: 6px; }
  .sidebar-item strong { font-weight: 700; }
  .letter-body {
    position: absolute;
    left: 115px;
    top: 153px;
    width: 374px;
    font-size: 8.35px;
    line-height: 11.85px;
    letter-spacing: 0.2px;
    color: var(--ink-body);
  }
  .letter-body p { margin-bottom: 11.85px; }
  .closing {
    position: absolute;
    left: 115px;
    top: 497px;
    font-size: 8px;
    color: var(--ink-body);
  }
  .signature {
    position: absolute;
    left: 114px;
    top: 508px;
    width: 162px;
    height: 22px;
    background: linear-gradient(90deg, rgba(42,42,42,0.14), rgba(42,42,42,0.05));
    border-radius: 3px;
  }
  .corner-block {
    position: absolute;
    left: 330px;
    top: 557px;
    width: 230px;
    height: 230px;
    border-radius: 12px 0 0 0;
    background: linear-gradient(90deg, var(--brand-green-light) 0%, var(--brand-green) 45%, var(--brand-blue) 60%, var(--brand-blue-deep) 100%);
  }
</style>
</head>
<body>
  <main class="letterhead">
    <header>
      <div class="brand">
        <span class="brand-square"></span>
        <span class="brand-name">Brightfold<br>Interiors Corp.</span>
      </div>
      <address class="contact">
        417 Brindlewood Avenue NE, Calgary, Alberta, Canada, T3M 4K8<br>
        phone: (403)582-3140
      </address>
    </header>

    <h1 class="letter-title">Lorem ipsum</h1>

    <aside class="sidebar">
      <div class="sidebar-item"><strong>Lorem ipsum</strong><br>dolor sit amet.</div>
      <div class="sidebar-item"><strong>Lorem</strong><br>ipsum dolor sit</div>
      <div class="sidebar-item"><strong>Lorem</strong><br>ipsum</div>
    </aside>

    <section class="letter-body">
      <p>Dolor sit amet, consectetur adipiscing elit. Morbi ut ipsum sit amet ipsum sodales venenatis at et arcu. Sed feugiat enim vitae bibendum condimentum. Aliquam vel mattis mauris. Aliquam nec dolor at neque rhoncus aliquam. Nam fringilla condimentum lacus, et posuere purus imperdiet ac. Suspendisse nisl eros, rhoncus a vestibulum vitae, fringilla in sem. Cras nec mauris nec leo viverra euismod in vel odio. In pellentesque dolor eu nunc tincidunt mollis. Mauris dignissim lectus at mauris egestas, in pharetra nisi hendrerit. Aenean sit amet ante sollicitudin, facilisis orci sit amet, dictum dolor. Nullam bibendum feugiat turpis, vitae aliquet nisi porttitor id. Vivamus erat lorem, imperdiet sed nulla sodales, sagittis lacinia urna. In a tristique felis. Ut dui diam, rhoncus eget gravida sit amet, convallis at eros. Integer cursus nec sem et lacinia.</p>
      <p>Nunc ligula odio, iaculis at ante eget, tincidunt adipiscing ante. Vestibulum mattis sapien dolor, porta porttitor urna dapibus sed. Nunc egestas ipsum et arcu fermentum, eget vulputate nunc semper. Ut volutpat venenatis porttitor. Proin accumsan cursus nisl et condimentum. Praesent tempus sapien quis augue feugiat, vitae auctor risus scelerisque. Nulla vehicula, dui in commodo lobortis, massa mi convallis mi, sit amet pellentesque ligula lorem at erat. Praesent porttitor lectus quis felis consectetur, id auctor dolor commodo. Curabitur dictum, libero in aliquam tincidunt, nunc tellus pretium tellus, sed facilisis magna dui at eros. Ut at orci aliquam, tincidunt nibh interdum, auctor ipsum. Ut molestie orci nec lectus vehicula vestibulum.</p>
      <p>Maecenas accumsan, augue et luctus semper, massa nulla fermentum est, ac dictum tellus lacus in erat. Aliquam tristique, augue et tristique ultricies, dui urna commodo justo, id convallis purus magna quis urna. Class aptent taciti sociosqu ad litora torquent per conubia nostra, per inceptos himenaeos. Vestibulum quis nibh nec arcu fringilla sollicitudin sed nec odio. Vestibulum adipiscing ligula sit amet lorem iaculis, quis venenatis turpis rhoncus. Praesent vitae pellentesque odio. Phasellus at magna luctus risus consectetur lobortis. Aliquam ac ultricies lorem, eget lobortis ante. Donec et nisl et sem ultrices hendrerit. In ullamcorper vitae enim non auctor. Fusce pharetra magna nec nisi laoreet iaculis. Phasellus rutrum lorem in leo dictum hendrerit. Praesent a mauris nec eros tempor facilisis.</p>
    </section>

    <div class="closing">Fusce scelerisque</div>
    <div class="signature" role="img" aria-label="Handwritten signature of the sender"></div>

    <div class="corner-block" aria-hidden="true"></div>
  </main>
</body>
</html>
```